wine label for ultra premium vineyard in Bendigo, Central Otago, New Zealand

"WREN" is our new wine brand, with grapes grown in our spectacular "ter Bosch" vineyard. The small, elevated vineyard overlooks a river valley and snowy mountains. We would like a highly elegant label for our 2018 pinot noir wine, which highlights the quality of wine and our very special vineyard location. "WREN" has to be prominent, with secondary emphasis on "ter Bosch vineyard" and "Bendigo, Central Otago". A stylized WREN logo (bird) could be a useful design device instead of the commonly seen illustrated mountain landscape (which is quite common for our local wines). Label size 90 high, 110 wide. Please use a pinot noir / burgundy bottle. See here for vineyard pics, and also below pics for other local wine labels and pics for inspiration / styles. https://www.instagram.com/jan.ter.bosch/

Target Market(s)

average bottle price for this premium red pinot noir would be aroundUS$40. target market are generally urban professionals aged 25 and older with a high degree of interest in pinot noir wine, and who are familiar with New Zealand pinot noir (ie. already know several brands).

Colors
ed252d

Requirements
Must have
• distinctive label, sophisticated look
Nice to have
• classy white paper stock
Should not have
• label must not get too busy... less but high quality and distinctive is more....

```html
<!DOCTYPE html>
<html lang="en">
<head>
<meta charset="utf-8">
<title>WREN – ter Bosch vineyard label</title>
<link rel="stylesheet" href="https://fonts.googleapis.com/css2?family=Cormorant+Garamond:wght@400&family=Josefin+Sans:wght@300&display=swap">
<style>
  :root {
    --backdrop: #b3202a;
    --label-dark: #1c1c1e;
    --label-mid: #2e2e31;
    --accent-red: #ed252d;
    --ink-white: #ffffff;
    --line-red: #d11f27;
  }
  * { margin: 0; padding: 0; box-sizing: border-box; }
  html, body {
    width: 1200px;
    height: 800px;
    overflow: hidden;
    background: var(--backdrop);
  }
  .canvas {
    position: relative;
    width: 1200px;
    height: 800px;
    display: flex;
    align-items: center;
    justify-content: center;
  }
  .label {
    position: relative;
    width: 660px;
    height: 540px;
    background: linear-gradient(180deg, var(--label-mid) 0%, var(--label-dark) 100%);
    overflow: hidden;
  }
  .label__texture {
    position: absolute;
    inset: 0;
    background: radial-gradient(ellipse at 60% 45%, rgba(70, 78, 96, 0.35) 0%, rgba(40, 42, 50, 0) 70%);
  }
  .label__rules {
    position: absolute;
    inset: 0;
    width: 660px;
    height: 540px;
  }
  .brand-name {
    position: absolute;
    left: 0;
    right: 0;
    top: 150px;
    display: flex;
    align-items: center;
    justify-content: center;
    gap: 28px;
  }
  .brand-name__dot {
    width: 46px;
    height: 46px;
    border-radius: 50%;
    background: var(--accent-red);
    flex: none;
  }
  .brand-name__text {
    font-family: "Josefin Sans", sans-serif;
    font-weight: 300;
    font-size: 84px;
    line-height: 1;
    letter-spacing: 0.22em;
    color: var(--ink-white);
    padding-top: 10px;
  }
  .vineyard-band {
    position: absolute;
    left: 130px;
    top: 318px;
    width: 400px;
    height: 42px;
    background: var(--accent-red);
    display: flex;
    align-items: center;
    justify-content: center;
    font-family: "Cormorant Garamond", serif;
    font-weight: 400;
    font-size: 32px;
    color: var(--ink-white);
  }
  .bird-motif {
    position: absolute;
    left: 50%;
    top: 378px;
    width: 90px;
    height: 62px;
    margin-left: -45px;
    background: linear-gradient(135deg, rgba(237, 37, 45, 0.35), rgba(237, 37, 45, 0.15));
    border-radius: 6px;
  }
  .region {
    position: absolute;
    left: 0;
    right: 0;
    top: 456px;
    text-align: center;
    font-family: "Josefin Sans", sans-serif;
    font-weight: 300;
    font-size: 20px;
    letter-spacing: 0.55em;
    color: var(--ink-white);
  }
</style>
</head>
<body>
  <main class="canvas">
    <section class="label">
      <div class="label__texture" role="img" aria-label="Faint flowing contour-line pattern in blue-grey across the label"></div>

      <svg class="label__rules" viewBox="0 0 660 540" aria-hidden="true">
        <line x1="0" y1="38" x2="610" y2="38" stroke="var(--line-red)" stroke-width="3"/>
        <line x1="610" y1="38" x2="640" y2="8" stroke="var(--line-red)" stroke-width="3"/>
        <line x1="0" y1="508" x2="610" y2="508" stroke="var(--line-red)" stroke-width="3"/>
        <line x1="610" y1="508" x2="640" y2="478" stroke="var(--line-red)" stroke-width="3"/>
        <line x1="622" y1="70" x2="660" y2="100" stroke="var(--line-red)" stroke-width="2"/>
        <line x1="612" y1="80" x2="650" y2="110" stroke="var(--line-red)" stroke-width="2"/>
        <line x1="622" y1="440" x2="660" y2="470" stroke="var(--line-red)" stroke-width="2"/>
        <line x1="612" y1="450" x2="650" y2="480" stroke="var(--line-red)" stroke-width="2"/>
      </svg>

      <div class="brand-name">
        <span class="brand-name__dot" aria-hidden="true"></span>
        <h1 class="brand-name__text">WREN</h1>
      </div>

      <p class="vineyard-band">ter Bosch vineyard</p>

      <div class="bird-motif" role="img" aria-label="Small red line drawing of three wrens perched together"></div>

      <p class="region">BENDIGO, CENTRAL OTAGO</p>
    </section>
  </main>
</body>
</html>
```